Dravetti Business Cards

We need a business card design for Dravetti Mining.

This is a B2B company that buys and sells large machinery tires within the coal mining industry. The design should the strong, crisp and masculine. I have uploaded the company logo and rough mock-up of what the back of the card should look like. the front of the card should have the same look/feel as the back. I need editable templates for both the front and the back of the card.

Color scheme should be grey/green/black

Contact information to include on the card:
Name: Owen Pellsworth
Title: Managing Director
Phone: 972-555-0143
Address: 3157 Brantley #5 Dallas, TX 75209
Email: Owen@Dravetti-example.com

I am also opening a contest for letterhead design. If you submit a business card design, please also submit a letterhead design with the same look/feel. The winner of the business card design will also will the letter head and be paid for both.

Target Market(s)

Procurement men/women in the coal mining industry

Industry/Entity Type

Coal Mining

```html
<!DOCTYPE html>
<html lang="en">
<head>
<meta charset="utf-8">
<title>Dravetti Mining — Business Card</title>
<link rel="stylesheet" href="https://fonts.googleapis.com/css2?family=Montserrat:wght@600;700&family=Questrial&display=swap">
<style>
  :root {
    --stage: #e6e7e8;
    --paper: #fbfbfa;
    --paper-shade: #eeeeee;
    --charcoal: #2b2c2e;
    --charcoal-deep: #1f2022;
    --ink-grey: #555759;
    --band-grey: #6b6d70;
    --green: #4fa521;
    --white: #ffffff;
  }
  * { box-sizing: border-box; margin: 0; padding: 0; }
  html, body {
    width: 1200px; height: 800px; overflow: hidden;
    background: var(--stage);
  }
  .stage {
    width: 1200px; height: 800px;
    display: flex; align-items: center; justify-content: center; gap: 40px;
  }
  .card {
    position: relative;
    width: 560px; height: 320px;
    overflow: hidden;
    box-shadow: 0 10px 28px rgba(0,0,0,0.18);
  }
  .card-front { background: var(--paper); }
  .card-back { background: linear-gradient(135deg, var(--charcoal) 0%, var(--charcoal-deep) 100%); }
  .card-shapes { position: absolute; inset: 0; }

  .wordmark {
    position: absolute;
    display: flex; align-items: center; gap: 12px;
    font-family: "Montserrat", sans-serif;
    font-weight: 700;
    text-transform: uppercase;
    letter-spacing: 0.04em;
    line-height: 1;
  }
  .wordmark-square { width: 16px; height: 16px; background: var(--green); }
  .card-front .wordmark { left: 44px; top: 62px; font-size: 30px; color: var(--ink-grey); }
  .card-back .wordmark {
    left: 50%; top: 50%; transform: translate(-50%, -50%);
    font-size: 34px; color: var(--white); white-space: nowrap;
  }

  .holder {
    position: absolute; right: 36px; top: 168px; text-align: right;
  }
  .holder-name {
    font-family: "Montserrat", sans-serif; font-weight: 700;
    font-size: 17px; color: var(--green); text-transform: uppercase; letter-spacing: 0.02em;
  }
  .holder-title {
    font-family: "Questrial", sans-serif; font-size: 13px; color: var(--ink-grey); margin-top: 3px;
  }

  .contact {
    position: absolute; left: 44px; top: 232px;
    font-family: "Questrial", sans-serif; font-size: 12.5px; color: var(--ink-grey);
    line-height: 1.6;
  }
  .contact-label { color: var(--green); font-weight: 700; }
</style>
</head>
<body>
<main class="stage">
  <section class="card card-front" aria-label="Card front">
    <svg class="card-shapes" viewBox="0 0 560 320" aria-hidden="true">
      <polygon points="420,0 560,0 560,150 470,150" fill="var(--paper-shade)"/>
      <polygon points="0,300 392,282 378,320 0,320" fill="var(--green)"/>
      <polygon points="392,282 560,272 560,320 378,320" fill="var(--band-grey)"/>
    </svg>
    <div class="wordmark"><span class="wordmark-square"></span>Dravetti Mining</div>
    <div class="holder">
      <p class="holder-name">Owen Pellsworth</p>
      <p class="holder-title">Managing Director</p>
    </div>
    <div class="contact">
      <p>3157 Brantley #5 Dallas, TX 75209 · <span class="contact-label">T:</span> 972-555-0143</p>
      <p><span class="contact-label">E:</span> owen@dravetti-example.com · <span class="contact-label">W:</span> www.dravetti-example.com</p>
    </div>
  </section>

  <section class="card card-back" aria-label="Card back">
    <div class="wordmark"><span class="wordmark-square"></span>Dravetti Mining</div>
  </section>
</main>
</body>
</html>
```